Lorvant Stationary and Branding Documents

Corporate Identity Branding stationary needed for IT Recruiting Firm.

I already have a Logo, business cards and website. I need to get designs completed for the remaining corporate identity documents.

The documentation should use similar colors as my website and business card. The designs should modern and clean.

http://lorvantsystems.example/

Target Market(s)

Information Technology Industry

Industry/Entity Type

Information Technology

Colors
3377b5
0255a3
fbee3e
f78f20
f37122
33a6d7
000000
0592cd

Requirements
Must have
• Letter Head
• Folder Design
• PowerPoint Design
• Invoice
• Envelope
Nice to have
• Proposal
• Flyer
• Brochure
Should not have
• Logo
• Business Cards
• Website

```html
<!DOCTYPE html>
<html lang="en">
<head>
<meta charset="utf-8">
<title>Lorvant Invoice 0001</title>
<link rel="stylesheet" href="https://fonts.googleapis.com/css2?family=Raleway:wght@300;400&display=swap">
<style>
  :root{
    --orange:#e07626;
    --blue:#0255a3;
    --grey-cell:#e4e4e4;
    --grey-line:#d2d2d2;
    --text:#6d6d6d;
    --paper:#f8f9f9;
    --backdrop:#c9d3f0;
  }
  *{box-sizing:border-box;margin:0;padding:0}
  html,body{width:1200px;height:784px;overflow:hidden}
  body{background:var(--backdrop);font-family:"Raleway",sans-serif;font-weight:300;color:var(--text);position:relative}
  .invoice{position:absolute;left:338px;top:20px;width:524px;height:744px;background:var(--paper);box-shadow:0 6px 18px rgba(40,60,140,.25);overflow:hidden}

  .invoice-head{position:absolute;left:38px;top:34px}
  .invoice-title{color:var(--orange);font-size:27px;font-weight:300;letter-spacing:.5px}
  .invoice-title b{font-weight:400}
  .invoice-dates{font-size:8.5px;line-height:12px;margin-top:4px}

  .brand{position:absolute;right:36px;top:40px;display:flex;align-items:center;gap:8px;color:var(--blue);font-size:34px;font-weight:300;letter-spacing:.5px}
  .brand-dot{width:11px;height:11px;background:var(--orange)}

  .parties{position:absolute;left:38px;top:112px;width:448px;height:130px;border:1px solid var(--orange);display:flex;gap:10px;padding:8px}
  .party{flex:1;display:flex;gap:6px}
  .party-mark{width:58px;height:46px;margin-top:24px;display:flex;align-items:center;justify-content:center;font-size:11px;color:var(--blue);border:1px solid var(--grey-line)}
  .party-mark.placeholder{color:#c6c6c6;font-size:10px;letter-spacing:1px}
  .party-body{flex:1}
  .party-label{background:var(--blue);color:#fff;font-size:9px;padding:5px 8px;height:20px;border-radius:0 0 3px 0}
  .party-line{background:var(--grey-cell);font-size:6.5px;height:14px;line-height:14px;padding-left:5px;margin-top:3px}

  .items-label{position:absolute;left:38px;top:256px;font-size:9px;letter-spacing:.5px}
  .items{position:absolute;left:38px;top:272px;width:448px;border-collapse:separate;border-spacing:0 3px;font-size:7.5px}
  .items th{background:var(--orange);color:#fff;font-weight:300;text-align:left;padding:6px 8px;font-size:8px}
  .items th:first-child{border-radius:6px 0 0 0}
  .items th:last-child{border-radius:0 0 6px 0}
  .items td{background:var(--grey-cell);height:22px;padding:0 8px;border-right:3px solid var(--paper)}
  .items td:last-child{border-right:0}
  .col-qty{width:52px;text-align:center}
  .col-price,.col-total{width:66px;text-align:right}

  .notes{position:absolute;left:38px;top:488px;width:222px;height:160px;border:1px solid var(--grey-line);padding:10px}
  .notes-title{font-size:9px;text-align:center;margin-bottom:6px}
  .notes-rule{border-bottom:1px solid var(--grey-line);height:22px}
  .notes-text{position:absolute;left:10px;top:150px;font-size:6.5px;white-space:nowrap;top:auto;bottom:-16px}

  .amount{position:absolute;left:288px;top:488px;width:198px}
  .amount-head{background:var(--blue);color:#fff;font-size:12px;padding:8px 10px;text-align:right;letter-spacing:.5px;border-radius:6px 0 0 0}
  .amount-row{display:flex;justify-content:space-between;align-items:center;background:var(--grey-cell);margin-top:3px;height:22px;padding:0 10px;font-size:7.5px}
  .amount-total{height:34px;font-size:8px}
  .amount-total strong{font-weight:300;font-size:19px}

  .footer-band{position:absolute;left:0;right:0;bottom:0;height:62px;background:var(--orange)}
</style>
</head>
<body>
<main class="invoice">
  <header class="invoice-head">
    <h1 class="invoice-title">Invoice <b>0001</b></h1>
    <p class="invoice-dates">01 September 2012<br>Payment due by 25 November 2012</p>
  </header>

  <div class="brand"><span class="brand-dot"></span>Lorvant</div>

  <section class="parties">
    <div class="party">
      <div class="party-mark">Lorvant</div>
      <div class="party-body">
        <div class="party-label">FROM</div>
        <div class="party-line">Your Address</div>
        <div class="party-line">Address Line 1</div>
        <div class="party-line">Town</div>
        <div class="party-line">Region/State</div>
        <div class="party-line">Zip/Postal Code</div>
      </div>
    </div>
    <div class="party">
      <div class="party-mark placeholder">LOGO</div>
      <div class="party-body">
        <div class="party-label">TO</div>
        <div class="party-line">Your Address</div>
        <div class="party-line">Address Line 1</div>
        <div class="party-line">Town</div>
        <div class="party-line">Region/State</div>
        <div class="party-line">Zip/Postal Code</div>
      </div>
    </div>
  </section>

  <p class="items-label">ITEMS</p>
  <table class="items">
    <thead>
      <tr><th class="col-qty">Quantity</th><th>Description</th><th class="col-price">Unit Price</th><th class="col-total">TOTAL</th></tr>
    </thead>
    <tbody>
      <tr><td class="col-qty">2</td><td>Donec ac erat vel neque molestie convallis.</td><td class="col-price">$600</td><td class="col-total">$1200</td></tr>
      <tr><td class="col-qty">1</td><td>Sed eget risus ac lacus tempus sollicitudin in ut magna.</td><td class="col-price">$300</td><td class="col-total">$300</td></tr>
      <tr><td class="col-qty">3</td><td>Nunc auctor nisl vel lorem aliquet pellentesque.</td><td class="col-price">$800</td><td class="col-total">$2400</td></tr>
      <tr><td class="col-qty">2</td><td>Pellentesque habitant morbi.</td><td class="col-price">$20</td><td class="col-total">$40</td></tr>
      <tr><td class="col-qty">2</td><td>In hac habitasse platea dictumst mauris ut.</td><td class="col-price">$2500</td><td class="col-total">$5000</td></tr>
      <tr><td class="col-qty">1</td><td>Aenean eget enim eget augue dictum fringilla et vitae.</td><td class="col-price">$100</td><td class="col-total">$100</td></tr>
    </tbody>
  </table>

  <section class="notes">
    <h2 class="notes-title" style="font-weight:300">Special Notes</h2>
    <div class="notes-rule"></div>
    <div class="notes-rule"></div>
    <div class="notes-rule"></div>
    <div class="notes-rule"></div>
    <div class="notes-rule"></div>
    <p class="notes-text">molestie condimentum. Curabitur nisi, faucibus sed</p>
  </section>

  <section class="amount">
    <div class="amount-head">AMOUNT DUE</div>
    <div class="amount-row"><span>SUBTOTAL</span><span>$9,040</span></div>
    <div class="amount-row"><span>TAX</span><span>$00.00</span></div>
    <div class="amount-row"><span>SHIPPING</span><span>$00.00</span></div>
    <div class="amount-row amount-total"><span>TOTAL</span><strong>$9,040.00</strong></div>
  </section>

  <div class="footer-band"></div>
</main>
</body>
</html>
```